NOT HAPPY FLYER

The brochure is for a Real Estate Agent, as a prospecting tool for upmarket, expensive homes.

BRIEF:
On the first side will be:
NOT HAPPY? (in a funky font)
(Have a picture of maybe an unhappy dog, or something that displays unhappiness on the front)

The second side:
-With your current service and advice?
Need a result NOW?
-Want a second opinion?

If you have been on the market for over 45 days with no results, it’s time to question why.

Nora Pemberley (photo of Nora)
Your Modern, Local Real Estate Agent.

It is no secret that the greater the exposure a property has to the market, the greater the number of buyers who are aware of the listing. Every property is unique and Nora ensures that each property has its own tailored marketing plan, so your property stands out from the crowd.

Whether you’re considering buying locally or internationally, Nora will work with you to towards understanding those special qualities and those requirements you seek.
If you want to combine these components into an advantageous world class real estate transaction, call Nora Pemberley.

W: (WEBSITE HERE)
M: (MOBILE HERE)
E: (EMAIL HERE)

Target Market(s)

The target market are people who own upmarket, expensive properties.

Industry/Entity Type

Real Estate

Font styles to use
Decorative

Requirements
Must have
• Must be fun, yet professional. Needs to stand out. It will be printed in matt gloss laminate, so it will look very exclusive.

Second side with my photo and a small Hovel logo
Nice to have
• Have some funky fonts.

```html
<!DOCTYPE html>
<html lang="en">
<head>
<meta charset="utf-8">
<title>Not Happy Flyer – Nora Pemberley</title>
<link href="https://fonts.googleapis.com/css2?family=Tenor+Sans&family=Courgette&family=Lobster+Two:ital,wght@1,700&family=Open+Sans:wght@400;600;700&display=swap" rel="stylesheet">
<style>
  :root {
    --orange: #fbae3c;
    --charcoal: #3d3d3f;
    --paper: #f2f2f2;
    --white: #ffffff;
    --stage: #e9e6e1;
    --photo-dog-a: #8a7d70;
    --photo-dog-b: #d9d2c8;
    --photo-agent-a: #6f7d5a;
    --photo-agent-b: #3a2e2a;
  }
  * { box-sizing: border-box; margin: 0; padding: 0; }
  html, body {
    width: 1200px; height: 899px; overflow: hidden;
    background: var(--stage);
    font-family: "Open Sans", Arial, sans-serif;
  }
  .canvas { position: relative; width: 1200px; height: 899px; }

  .flyer {
    position: absolute; width: 560px; height: 793px; overflow: hidden;
    background: var(--white);
  }
  .flyer--front { left: 24px; top: 27px; }
  .flyer--back { left: 612px; top: 67px; }

  .contact-bar {
    position: absolute; left: 0; bottom: 0; width: 100%; height: 40px;
    background: var(--charcoal); color: var(--white);
    display: flex; align-items: center; justify-content: space-between;
    padding: 0 24px 0 12px; font-size: 11.5px; font-weight: 600;
  }
  .contact-item { display: flex; align-items: center; gap: 7px; }
  .contact-item svg { width: 13px; height: 13px; }
  .contact-item--phone { font-size: 14px; }
  .contact-item--phone svg { width: 17px; height: 17px; }

  /* Front */
  .front-photo {
    position: absolute; left: 0; top: 0; width: 560px; height: 466px;
    background: radial-gradient(ellipse at 45% 55%, var(--photo-dog-b) 0%, var(--photo-dog-b) 30%, var(--photo-dog-a) 75%);
  }
  .front-band {
    position: absolute; left: 0; top: 466px; width: 560px; height: 287px;
    background: var(--orange);
  }
  .headline-not {
    position: absolute; left: 54px; top: 22px;
    font-family: "Tenor Sans", Helvetica, sans-serif;
    font-size: 140px; line-height: 1; color: var(--charcoal); letter-spacing: -10px;
  }
  .headline-happy {
    position: absolute; left: 176px; top: 140px;
    font-family: "Courgette", cursive;
    font-size: 86px; line-height: 1.1; color: var(--white);
  }
  .headline-mark {
    position: absolute; left: 438px; top: 150px;
    font-family: "Tenor Sans", Helvetica, sans-serif;
    font-size: 150px; line-height: 0.8; color: var(--charcoal);
  }

  /* Back */
  .back-header {
    position: absolute; left: 0; top: 0; width: 560px; height: 217px;
    background: var(--charcoal); color: var(--white);
  }
  .question {
    position: absolute; text-align: right; white-space: nowrap;
    font-family: "Lobster Two", cursive; font-style: italic; font-weight: 700;
    font-size: 25px; line-height: 1;
  }
  .question--service { top: 48px; right: 152px; }
  .question--result {
    top: 96px; right: 154px; color: var(--orange);
    font-family: "Tenor Sans", Helvetica, sans-serif; font-style: normal; font-weight: 400;
    display: flex; align-items: baseline; gap: 10px;
  }
  .question--result .lead { font-size: 22px; font-variant: small-caps; letter-spacing: 1px; }
  .question--result .now { font-size: 56px; line-height: 0.8; }
  .question--opinion { top: 158px; right: 164px; }
  .header-mark {
    position: absolute; right: 36px; top: 36px;
    font-family: "Tenor Sans", Helvetica, sans-serif;
    font-size: 210px; line-height: 0.8; color: var(--orange);
  }

  .agent-column {
    position: absolute; left: 0; top: 217px; width: 222px; height: 536px;
    background: var(--orange); text-align: center;
  }
  .agent-pitch {
    margin-top: 27px; color: var(--white);
    font-weight: 700; font-size: 14px; line-height: 29px;
  }
  .agent-photo {
    position: absolute; left: 20px; top: 209px; width: 181px; height: 256px;
    background: linear-gradient(180deg, var(--photo-agent-a) 0%, var(--photo-agent-a) 35%, var(--photo-agent-b) 100%);
  }
  .agent-name {
    position: absolute; left: 0; top: 474px; width: 100%;
    font-size: 19px; font-weight: 700; color: var(--charcoal);
  }
  .agent-role {
    position: absolute; left: 0; top: 508px; width: 100%;
    font-size: 10.5px; color: var(--charcoal);
  }

  .copy-panel {
    position: absolute; left: 222px; top: 217px; width: 338px; height: 536px;
    background: var(--paper); color: var(--charcoal);
    padding: 22px 14px 0 22px;
    font-size: 14.5px; line-height: 20.5px;
  }
  .copy-panel p.gap { margin-top: 40px; }
  .copy-panel p.gap-sm { margin-top: 20px; }
  .copy-panel strong { font-weight: 700; }

  .brand-mark {
    position: absolute; left: 0; top: 448px; width: 364px;
    display: flex; align-items: center; justify-content: center; gap: 8px;
    font-size: 20px; font-weight: 700; color: var(--charcoal);
  }
  .brand-mark .brand-square { width: 14px; height: 14px; background: var(--charcoal); }
</style>
</head>
<body>
<main class="canvas">

  <section class="flyer flyer--front">
    <div class="front-photo" role="img" aria-label="Photo of a sad-looking white and tan bulldog puppy sitting on wooden decking"></div>
    <div class="front-band">
      <div class="headline-not">NOT</div>
      <div class="headline-happy">happy</div>
      <div class="headline-mark">?</div>
    </div>
    <footer class="contact-bar">
      <span class="contact-item">
        <svg viewBox="0 0 16 16" aria-hidden="true"><rect x="1" y="3" width="14" height="10" rx="2" fill="#fff"/><path d="M2 4l6 5 6-5" stroke="#3d3d3f" stroke-width="1.4" fill="none"/></svg>
        nora.pemberley@hovelmail.com
      </span>
      <span class="contact-item">
        <svg viewBox="0 0 16 16" aria-hidden="true"><circle cx="8" cy="8" r="6.5" fill="none" stroke="#fff" stroke-width="1.6"/><path d="M1.5 8h13M8 1.5c-3 3.5-3 9.5 0 13M8 1.5c3 3.5 3 9.5 0 13" stroke="#fff" stroke-width="1.2" fill="none"/></svg>
        www.hovelhomes.com
      </span>
      <span class="contact-item contact-item--phone">
        <svg viewBox="0 0 16 16" aria-hidden="true"><circle cx="8" cy="8" r="7.2" fill="none" stroke="#fff" stroke-width="1.3"/><path d="M5.2 4.2l1.4 1.6-.8 1.2c.6 1.3 1.6 2.3 2.9 2.9l1.2-.8 1.6 1.4-.9 1.3c-3-.4-5.7-3.1-6.1-6.1z" fill="#fff"/></svg>
        000 000 000
      </span>
    </footer>
  </section>

  <section class="flyer flyer--back">
    <header class="back-header">
      <div class="question question--service">with your current service and advice</div>
      <div class="question question--result"><span class="lead">Need a result</span><span class="now">NOW</span></div>
      <div class="question question--opinion">want a second opinion</div>
      <div class="header-mark">?</div>
    </header>

    <aside class="agent-column">
      <p class="agent-pitch">If you have been<br>on the<br>market for over 45 days<br>with no results,<br>it’s time to question why.</p>
      <div class="agent-photo" role="img" aria-label="Portrait photo of agent Nora Pemberley"></div>
      <div class="agent-name">Nora Pemberley</div>
      <div class="agent-role">Your Modern, Local Real Estate Agent</div>
    </aside>

    <article class="copy-panel">
      <p>It is no secret that the greater the exposure a property has to the market, the greater the number of buyers who are aware of the listing.</p>
      <p>Every property is unique and <strong>Nora</strong> ensures that each property has its own tailored marketing plan, so your property stands out from the crowd.</p>
      <p class="gap">Whether you’re considering buying locally or internationally, <strong>Nora</strong> will work with you to towards understanding those special qualities and those requirements you seek.</p>
      <p class="gap-sm">If you want to combine these components into an advantageous world class real estate transaction, call <strong>Nora Pemberley.</strong></p>
      <div class="brand-mark"><span class="brand-square"></span>Hovel</div>
    </article>

    <footer class="contact-bar">
      <span class="contact-item">
        <svg viewBox="0 0 16 16" aria-hidden="true"><rect x="1" y="3" width="14" height="10" rx="2" fill="#fff"/><path d="M2 4l6 5 6-5" stroke="#3d3d3f" stroke-width="1.4" fill="none"/></svg>
        nora.pemberley@hovelmail.com
      </span>
      <span class="contact-item">
        <svg viewBox="0 0 16 16" aria-hidden="true"><circle cx="8" cy="8" r="6.5" fill="none" stroke="#fff" stroke-width="1.6"/><path d="M1.5 8h13M8 1.5c-3 3.5-3 9.5 0 13M8 1.5c3 3.5 3 9.5 0 13" stroke="#fff" stroke-width="1.2" fill="none"/></svg>
        www.hovelhomes.com
      </span>
      <span class="contact-item contact-item--phone">
        <svg viewBox="0 0 16 16" aria-hidden="true"><circle cx="8" cy="8" r="7.2" fill="none" stroke="#fff" stroke-width="1.3"/><path d="M5.2 4.2l1.4 1.6-.8 1.2c.6 1.3 1.6 2.3 2.9 2.9l1.2-.8 1.6 1.4-.9 1.3c-3-.4-5.7-3.1-6.1-6.1z" fill="#fff"/></svg>
        000 000 000
      </span>
    </footer>
  </section>

</main>
</body>
</html>
```